MY BEST MARKETING TOOL 8 PAGE FULL COLOR BOOKLET TO PHYSICIANS

I HAVE CORRECT DATA IN RIGHT PLACES. NEED HELP WITH FINISHING TOUCHES TO MAKE IT LOOK PROFESSIONAL AND GET IT PRINT READY. I HAVE USED CANVA TO GET THIS FAR. SO IF I NEED TO SHARE CANVA WITH YOU, HAPPY TO DO SO. THESE BOOKLETS WILL BE USED IN MARKETING. AUDIENCE IS DOCTORS. I WANT INFO TO BE CLEAR AND EASY TO FOLLOW.
Updates

MY FAVORITE COLORS ARE NAVY BLUE, COLUMBIA (SKY BLUE), LIGHT GRAY, SILVER, AND WHITE. THINK THESE SHOULD BE BASIC COLOR RANGE.

TRY TO USE LARGER TEXT PLEASE.

WEBSITE FOR BUSINESS---------------BRAVELTON318.COM

Target Market(s)

FAMILY MEDICINE PHYSICIANS

Industry/Entity Type

MEDICAL

Font styles to use
Other font styles liked:
• CEREBRI, CODE PRO

Colors
0054AA
0677BA
7BADD7
CADEEF
E8F1F8

Requirements
Must have
• CLEAN, NEAT, CLEAR, BUT VERY PROFESSIONAL LOOK
Nice to have
• IMPROVE LAYOUT/GRAPHICS/TABLES/BOXES/DIFFERENT COLOR TEXT IN PLACES, I LIKE PAGES WITH FULL BORDER OR SPLIT PAGE INTO 2 WITH SOME GRAPHIC. ETC.
Should not have
• DONT WANT FANCY. ALL PROFESSIONAL

```html
<!DOCTYPE html>
<html lang="en">
<head>
<meta charset="utf-8">
<title>Bravelton – Chronic Care Booklet</title>
<link rel="stylesheet" href="https://fonts.googleapis.com/css2?family=Montserrat:wght@300;400;600&family=Poppins:wght@400;500;600&display=swap">
<style>
  :root {
    --canvas: #f6f4f4;
    --paper: #ffffff;
    --navy: #0b4787;
    --navy-soft: #22589a;
    --silver: #b3c0cf;
    --mist: #f3f3f3;
    --ink: #1a1a1a;
    --icon: #1f4e8c;
  }
  * { box-sizing: border-box; margin: 0; padding: 0; }
  html, body { width: 1200px; height: 3000px; overflow: hidden; }
  body { background: var(--canvas); font-family: "Poppins", sans-serif; color: var(--ink); position: relative; }

  .page { position: absolute; left: 249px; width: 650px; height: 842px; background: var(--paper); box-shadow: 0 2px 10px rgba(0,0,0,.05); overflow: hidden; }
  .page--cover { top: 85px; }
  .page--founder { top: 1080px; }
  .page--services { top: 2061px; }

  /* Cover */
  .cover__roofline { position: absolute; left: 360px; top: 161px; width: 290px; height: 18px; background: var(--silver); }
  .cover__band { position: absolute; left: 0; top: 179px; width: 650px; height: 544px; background: var(--navy); color: #fff; text-align: center; }
  .cover__name { position: absolute; left: 0; right: 0; top: 230px; display: flex; align-items: center; justify-content: center; gap: 14px; font-family: "Montserrat", sans-serif; font-weight: 300; font-size: 46px; letter-spacing: 1px; }
  .cover__name-mark { width: 18px; height: 18px; background: var(--silver); }
  .cover__rule { position: absolute; left: 184px; top: 315px; width: 282px; height: 2px; background: var(--silver); }
  .cover__tagline { position: absolute; left: 0; right: 0; top: 340px; font-family: "Montserrat", sans-serif; font-weight: 400; font-size: 14px; letter-spacing: 6px; line-height: 20px; color: #dfe6ef; }
  .cover__motto { position: absolute; left: 0; right: 0; top: 432px; font-family: "Montserrat", sans-serif; font-weight: 600; font-size: 15px; letter-spacing: 3px; }
  .cover__web { position: absolute; left: 335px; top: 764px; display: flex; align-items: center; gap: 8px; font-size: 17px; color: var(--ink); }

  /* Founder */
  .founder__backdrop { position: absolute; left: 0; top: 0; width: 574px; height: 346px; background: var(--mist); }
  .founder__panel { position: absolute; left: 126px; top: 254px; width: 524px; height: 534px; background: var(--navy-soft); }
  .founder__photo { position: absolute; left: 174px; top: 70px; width: 442px; height: 424px; background: linear-gradient(180deg, #dfe4ea 0%, #b9c6d6 45%, #7d93b3 100%); }
  .founder__bio { position: absolute; left: 174px; top: 545px; width: 410px; font-size: 15.5px; line-height: 19.3px; color: #fff; }

  /* Services */
  .services__photo { position: absolute; left: 34px; top: 36px; width: 259px; height: 237px; background: linear-gradient(135deg, #e9e4de 0%, #8a8d93 50%, #2f3236 100%); }
  .services__label { position: absolute; left: 252px; top: 148px; width: 311px; height: 47px; background: var(--silver); }
  .services__title { position: absolute; left: 298px; font-weight: 600; font-size: 22px; color: var(--ink); }
  .services__title--ccm { top: 158px; }
  .services__title--bhi { top: 206px; }
  .services__aside { position: absolute; left: 174px; top: 312px; width: 476px; height: 468px; background: var(--mist); }
  .services__intro { position: absolute; left: 0; top: 273px; width: 563px; height: 131px; background: var(--navy); color: #fff; padding: 28px 20px 0 86px; font-size: 17.5px; line-height: 23.5px; }
  .services__list { position: absolute; left: 0; top: 0; width: 650px; height: 842px; list-style: none; }
  .service { position: absolute; left: 0; width: 650px; display: flex; align-items: center; transform: translateY(-50%); }
  .service__leader { width: 158px; border-top: 2px dotted #555; margin-right: 44px; }
  .service__icon { width: 50px; height: 50px; flex: none; }
  .service__text { margin-left: 24px; width: 300px; font-size: 15.5px; line-height: 18px; color: var(--ink); }
</style>
</head>
<body>

<section class="page page--cover">
  <div class="cover__roofline"></div>
  <div class="cover__band">
    <div class="cover__name"><span class="cover__name-mark"></span>BRAVELTON</div>
    <div class="cover__rule"></div>
    <p class="cover__tagline">CHRONIC CARE<br>EXPERTS</p>
    <p class="cover__motto">SAVING LIVES 24/7</p>
  </div>
  <div class="cover__web">
    <svg width="18" height="18" viewBox="0 0 18 18" fill="none" stroke="#222" stroke-width="1.3"><circle cx="9" cy="9" r="7.5"/><ellipse cx="9" cy="9" rx="3.3" ry="7.5"/><path d="M1.5 9h15M3 5h12M3 13h12"/></svg>
    <span>www.yourwebsite,com</span>
  </div>
</section>

<section class="page page--founder">
  <div class="founder__backdrop"></div>
  <div class="founder__panel"></div>
  <div class="founder__photo" role="img" aria-label="Family portrait of the founder with his wife and three daughters on a sandy beach"></div>
  <p class="founder__bio">Daniel Harwick, RN, BSN started Bravelton One, LLC in 2022 to provide Chronic Care Services with the mission to help people stay at home and out of the hospital. His first job was an orderly in the hospital at age 17. In the past 35 years, he has successfully started, grown, and sold a Physical Therapy clinic, a Home Medical Equipment company, and aSleep Lab. From 2015 to 2022, he worked as a Critical Care Travel Nurse in 5 states.</p>
</section>

<section class="page page--services">
  <div class="services__photo" role="img" aria-label="Hand lifting the receiver of a black desk telephone"></div>
  <div class="services__label"></div>
  <h2 class="services__title services__title--ccm">CCM- Chronic Care</h2>
  <h2 class="services__title services__title--bhi">BHI-Behavioral Health</h2>
  <div class="services__aside"></div>
  <p class="services__intro">A Registered Nurse will be accessible by phone 24 / 7 for addressing patient needs such as assessments, refills, education,and expediting sick visits.</p>

  <ul class="services__list">
    <li class="service" style="top:469px">
      <span class="service__leader"></span>
      <svg class="service__icon" viewBox="0 0 50 50" fill="none" stroke="var(--icon)" stroke-width="2"><path d="M5 22 25 6l20 16"/><path d="M10 18v26h30V18"/><circle cx="25" cy="29" r="9"/><path d="M25 24v10M20 29h10"/><path d="M5 44h40"/></svg>
      <span class="service__text">Assisting in referrals to specialists and home care services.</span>
    </li>
    <li class="service" style="top:559px">
      <span class="service__leader"></span>
      <svg class="service__icon" viewBox="0 0 50 50" fill="none" stroke="var(--icon)" stroke-width="2"><path d="M25 44C12 35 5 27 5 18a10 10 0 0 1 20-3 10 10 0 0 1 20 3c0 9-7 17-20 26z"/><circle cx="18" cy="21" r="3"/><circle cx="25" cy="19" r="3"/><circle cx="32" cy="21" r="3"/><path d="M14 31c0-4 8-4 8 0M21 29c0-4 8-4 8 0M28 31c0-4 8-4 8 0"/></svg>
      <span class="service__text">Assisting with social services, transportation, and medical equipment and supplies</span>
    </li>
    <li class="service" style="top:643px">
      <span class="service__leader"></span>
      <svg class="service__icon" viewBox="0 0 50 50" fill="none" stroke="var(--icon)" stroke-width="2"><path d="M25 4 8 10v14c0 11 7 18 17 22 10-4 17-11 17-22V10z"/><path d="M22 18h6v6h6v6h-6v6h-6v-6h-6v-6h6z"/></svg>
      <span class="service__text">Scheduling any preventive care needed.</span>
    </li>
    <li class="service" style="top:735px">
      <span class="service__leader"></span>
      <svg class="service__icon" viewBox="0 0 50 50" fill="none" stroke="var(--icon)" stroke-width="2"><rect x="5" y="8" width="24" height="30"/><circle cx="15" cy="20" r="5"/><path d="M15 15v-3M10 30h14"/><circle cx="38" cy="12" r="4"/><path d="M32 46V24h12v22M38 30v16"/><path d="M5 46h40"/></svg>
      <span class="service__text">Providing nutritional education and supporting positive lifestyle changes</span>
    </li>
  </ul>
</section>

</body>
</html>
```